QuillmarkAdvisory Business Card Design

Design business cards with attached ideas. I am open to several different ideas that would be interesting and innovative. What I have provided is logo and colors. Font should be Helvetica although it could be bold or light as needed. The design can be vertical or horizontal. The design should be more interesting than a standard business card. Files must be ready to send to a printer and in Illustrator format. The text with the five icons should be exact. Send me some ideas and I will get back to you right away. I need to choose a design within 3-5 days.

Target Market(s)

Business audience

Industry/Entity Type

Business

Contact Information for Business Card

Files should be ready to send to printer in illustrator format

Font styles to use
Sans Serif

Colors
3276b5

Requirements
Must have
• Use attached logo and two colors - blue / gray
• Include 5 offering icons and text on back
Nice to have
• Interesting and innovative design. Vertical or horizontal are both fine.

```html
<!DOCTYPE html>
<html lang="en">
<head>
<meta charset="utf-8">
<title>QuillmarkAdvisory Business Card</title>
<link rel="stylesheet" href="https://fonts.googleapis.com/css2?family=Arimo:wght@400;700&display=swap">
<style>
  :root {
    --brand-blue: #1d5a92;
    --ink: #111111;
    --card: #ffffff;
    --backdrop: #ecebe8;
    --rule: #333333;
  }
  * { margin: 0; padding: 0; box-sizing: border-box; }
  html, body { width: 1200px; height: 1000px; overflow: hidden; }
  body {
    background: var(--backdrop);
    font-family: "Arimo", Helvetica, Arial, sans-serif;
    color: var(--ink);
    position: relative;
  }
  .card {
    position: absolute;
    left: 287px;
    width: 626px;
    height: 368px;
    background: var(--card);
    border-radius: 18px;
    border: 1px solid #2b2b2b;
    box-shadow: 0 3px 10px rgba(0,0,0,0.18);
  }
  .card--front { top: 121px; }
  .card--back { top: 511px; }

  .brand-square {
    position: absolute;
    left: 270px; top: 21px;
    width: 86px; height: 87px;
    background: var(--brand-blue);
    border-radius: 5px;
  }
  .brand-name {
    position: absolute;
    left: 0; right: 0; top: 128px;
    text-align: center;
    font-size: 34px;
    font-weight: 700;
    color: var(--brand-blue);
    letter-spacing: -0.3px;
  }
  .tagline {
    position: absolute;
    left: 0; right: 0; top: 169px;
    text-align: center;
    font-size: 16px;
  }
  .person {
    position: absolute;
    left: 100px; width: 196px; top: 253px;
    text-align: center;
    line-height: 24px;
  }
  .person__name { font-size: 19px; }
  .person__name small { font-size: 17px; }
  .person__title { font-size: 17px; }
  .divider {
    position: absolute;
    left: 312px; top: 246px;
    width: 2px; height: 100px;
    background: var(--rule);
  }
  .contact {
    position: absolute;
    left: 344px; top: 249px;
    list-style: none;
    font-size: 18px;
    line-height: 30px;
  }

  .offerings-title {
    position: absolute;
    left: 171px; top: 30px;
    font-size: 17px;
  }
  .offerings-title strong { color: var(--brand-blue); font-weight: 700; }
  .offerings {
    position: absolute;
    left: 113px; top: 67px;
    list-style: none;
  }
  .offering {
    display: flex;
    align-items: center;
    height: 54.5px;
    font-size: 16.5px;
  }
  .offering svg { width: 44px; height: 44px; margin-right: 14px; flex: none; }
</style>
</head>
<body>
  <section class="card card--front" aria-label="Business card front">
    <div class="brand-square"></div>
    <div class="brand-name">QuillmarkAdvisory</div>
    <div class="tagline">Clear Thinking - Lasting Results</div>
    <div class="person">
      <div class="person__name">Dana Hollis, <small>PhD</small></div>
      <div class="person__title">Managing Director</div>
    </div>
    <div class="divider"></div>
    <ul class="contact">
      <li>555-014-2287</li>
      <li>Dana@QuillmarkAdvisory.com</li>
      <li>QuillmarkAdvisory.com</li>
    </ul>
  </section>

  <section class="card card--back" aria-label="Business card back">
    <div class="offerings-title"><strong>QuillmarkAdvisory</strong> Offerings</div>
    <ul class="offerings">
      <li class="offering">
        <svg viewBox="0 0 44 44" aria-hidden="true">
          <circle cx="22" cy="22" r="22" fill="var(--brand-blue)"/>
          <rect x="12" y="13" width="20" height="17" fill="none" stroke="#fff" stroke-width="2"/>
          <rect x="15" y="16" width="5" height="5" fill="#fff"/>
          <path d="M22 17h7M22 20h7M15 24h14M15 27h14" stroke="#fff" stroke-width="1.5"/>
        </svg>
        <span>Concepts: Thought leadership white papers</span>
      </li>
      <li class="offering">
        <svg viewBox="0 0 44 44" aria-hidden="true">
          <circle cx="22" cy="22" r="22" fill="var(--brand-blue)"/>
          <circle cx="22" cy="15" r="4" fill="#fff"/>
          <path d="M15 27c0-5 3-7 7-7s7 2 7 7z" fill="#fff"/>
          <rect x="11" y="28" width="22" height="3" fill="#fff"/>
        </svg>
        <span>Curriculum: Short courses on strategy</span>
      </li>
      <li class="offering">
        <svg viewBox="0 0 44 44" aria-hidden="true">
          <circle cx="22" cy="22" r="22" fill="var(--brand-blue)"/>
          <circle cx="12" cy="14" r="2.5" fill="#fff"/>
          <rect x="10" y="17" width="4" height="12" fill="#fff"/>
          <circle cx="32" cy="14" r="2.5" fill="#fff"/>
          <rect x="30" y="17" width="4" height="12" fill="#fff"/>
          <path d="M17 19h10l-2-2M27 24H17l2 2" stroke="#fff" stroke-width="1.6" fill="none"/>
        </svg>
        <span>Couching: Building your strategic leadership</span>
      </li>
      <li class="offering">
        <svg viewBox="0 0 44 44" aria-hidden="true">
          <circle cx="22" cy="22" r="22" fill="var(--brand-blue)"/>
          <circle cx="22" cy="23" r="8" fill="none" stroke="#fff" stroke-width="1.3" stroke-dasharray="2 2"/>
          <circle cx="22" cy="13" r="3" fill="#fff"/>
          <circle cx="13" cy="29" r="3" fill="#fff"/>
          <circle cx="31" cy="29" r="3" fill="#fff"/>
        </svg>
        <span>Consulting: Developing your strategic future</span>
      </li>
      <li class="offering">
        <svg viewBox="0 0 44 44" aria-hidden="true">
          <circle cx="22" cy="22" r="22" fill="var(--brand-blue)"/>
          <circle cx="13" cy="15" r="2.5" fill="#fff"/>
          <rect x="11" y="18" width="4" height="13" fill="#fff"/>
          <rect x="18" y="13" width="16" height="11" fill="none" stroke="#fff" stroke-width="1.5"/>
          <path d="M20 22l4-4 3 2 5-5" stroke="#fff" stroke-width="1.5" fill="none"/>
        </svg>
        <span>ScoreCard: Balanced ScoreCard and software</span>
      </li>
    </ul>
  </section>
</body>
</html>
```